Website design for Maple Nook Kidcare

I need a website designed for my daycare business, Maple Nook Kidcare, now that I have a new logo. My former website was ok but simple and I did not have a logo yet. It also was created by me using a template and was entirely pink. I loved the bright, happy feel of it but worried it might not appeal as much to potential clients who have sons. Therefore, I need a site which will appeal to both genders while still keeping the cheerful color scheme of my new logo, which has pinks, blue, green and cream.

Reason: Hello! I am still trying to download my new logo and am sorry it is taking me so long. Hopefully I will it posted by the end of today (US Eastern Standard Time). Thank you all very much for your patience!

Hello! I have finally managed to upload my new logo for you to use in designing my website. I'm sorry it took so long and greatly appreciate your time and creative efforts! I look forward to seeing what is submitted based on my logo design and its style/colors.

Many thanks!

Reason: As I've been traveling and posted my logo file late, I am extending my deadline. I am now back and can focus on providing more and better feedback. I appreciate your patience and submissions very much!

Reason: I need more time to provide feedback and make decisions.

Industry/Entity Type

Daycare

Colors
0192cd
33a6d7
86cae7
cadf82
fbf289
add136
e34197

```html
<!DOCTYPE html>
<html lang="en">
<head>
<meta charset="utf-8">
<title>Maple Nook Kidcare</title>
<link href="https://fonts.googleapis.com/css2?family=Bevan&display=swap" rel="stylesheet">
<style>
:root{
  --sky-top:#dff1fb;
  --sky-mid:#86cae7;
  --sky-low:#5fb3e0;
  --grass-light:#cadf82;
  --grass:#9cc74a;
  --ribbon:#2a8ed0;
  --ribbon-dark:#1c72b0;
  --green-head:#8cc63f;
  --text:#555555;
  --text-dark:#404040;
  --orange:#f26b3a;
  --pink:#e04a74;
  --purple:#7b64ae;
  --white:#ffffff;
  --logo-pink:#e34197;
}
*{margin:0;padding:0;box-sizing:border-box}
html,body{width:1191px;height:1200px;overflow:hidden}
body{position:relative;font-family:Arial,Helvetica,sans-serif;background:var(--sky-top)}
.scene{position:absolute;inset:0;background:linear-gradient(180deg,var(--sky-top) 0%,#bfe3f6 12%,var(--sky-mid) 35%,var(--sky-low) 62%,var(--grass-light) 78%,var(--grass) 100%)}
.art{position:absolute;border-radius:24px 24px 0 0}
.art-kids-top{left:200px;top:6px;width:240px;height:151px;background:linear-gradient(180deg,#f3dcc8,#cfe8f5);opacity:.8}
.art-top-right{left:730px;top:8px;width:350px;height:149px;background:linear-gradient(180deg,#e6f3fb,#c4e3f4);opacity:.9}
.logo{position:absolute;left:470px;top:80px;width:250px;text-align:center;font-family:'Bevan',Georgia,serif;font-size:26px;line-height:30px;color:var(--logo-pink)}
.panel{position:absolute;left:110px;top:157px;width:980px;height:981px;background:var(--white);border-radius:8px}
.hero{position:absolute;left:124px;top:172px;width:952px;height:295px;border-radius:8px;background:linear-gradient(90deg,#f6a06a 0%,#e9e4df 30%,#f2eee9 60%,#e6dccf 100%)}
.ribbon-tail{position:absolute;top:510px;width:50px;height:50px;background:var(--ribbon-dark)}
.ribbon-tail.left{left:63px;clip-path:polygon(0 0,100% 0,100% 100%,0 100%,22% 50%)}
.ribbon-tail.right{left:1088px;clip-path:polygon(0 0,100% 0,78% 50%,100% 100%,0 100%)}
.nav{position:absolute;left:93px;top:481px;width:1014px;height:48px;background:var(--ribbon);border-radius:6px;display:flex;justify-content:center;align-items:center;gap:28px}
.nav a{font-family:'Bevan',Georgia,serif;font-size:17px;color:var(--white);text-decoration:none}
.welcome-title{position:absolute;left:137px;top:550px;width:910px;font-family:'Bevan',Georgia,serif;font-weight:400;font-size:22px;line-height:29px;letter-spacing:.3px;color:var(--green-head)}
.intro{position:absolute;left:136px;top:622px;width:925px;font-size:14px;line-height:17px;color:var(--text)}
.intro p+p{margin-top:16px}
.news{position:absolute;left:137px;top:770px;width:195px}
.news h2{font-family:'Bevan',Georgia,serif;font-weight:400;font-size:23px;line-height:30px;color:var(--text-dark);margin-bottom:16px}
.news p{font-size:14px;line-height:17px;color:var(--text)}
.news p+p{margin-top:16px}
.card{position:absolute;top:815px;width:235px;border-radius:8px;color:var(--white);padding:0 22px 0 26px}
.card h3{font-family:'Bevan',Georgia,serif;font-size:23px;line-height:30px;text-align:center;font-weight:400;margin-bottom:4px}
.card p{font-size:14px;line-height:17px}
.card-learning{left:356px;height:199px;background:var(--orange);padding-top:50px}
.card-creativity{left:601px;height:248px;background:var(--pink);padding:54px 18px 0 22px}
.card-sharing{left:846px;height:303px;background:var(--purple);padding:54px 22px 0 27px}
.card-sharing p,.card-creativity p{margin-top:4px}
.figure{position:absolute;border-radius:40px;opacity:.85}
.fig-pencil{left:390px;top:722px;width:160px;height:118px;background:linear-gradient(135deg,#f7d14a,#e7604a)}
.fig-painter{left:650px;top:690px;width:140px;height:168px;background:linear-gradient(180deg,#9fd4f2,#f0a8c0)}
.fig-pair{left:895px;top:710px;width:150px;height:128px;background:linear-gradient(135deg,#f4d77a,#6fc1d8)}
.footer{position:absolute;top:1153px;left:117px;width:959px;display:flex;justify-content:space-between;font-size:14px;color:var(--white)}
</style>
</head>
<body>
<div class="scene" role="img" aria-label="Cartoon sky with clouds, trees, butterflies and rolling green hills"></div>
<div class="art art-kids-top" role="img" aria-label="Two cartoon children running"></div>
<div class="art art-top-right" role="img" aria-label="Cartoon rainbow ending in a cloud"></div>
<div class="logo">Maple Nook Kidcare</div>

<div class="panel"></div>
<div class="hero" role="img" aria-label="Photo of three toddlers playing with colourful balls"></div>

<div class="ribbon-tail left"></div>
<div class="ribbon-tail right"></div>
<nav class="nav">
  <a href="#">Home</a><a href="#">About Us</a><a href="#">Services</a><a href="#">Hours and Fees</a><a href="#">Policies</a><a href="#">Contact Us</a><a href="#">Photos</a><a href="#">Testimonials</a>
</nav>

<h1 class="welcome-title">Welcome to Maple Nook Kidcare, a playspace where children can play, create, and imagine!</h1>
<div class="intro">
  <p>Welcome to Maple Nook Kidcare, a licensed Group Family Day Care, located in Riverton's beautiful Hillcrest district. We are located on a pretty, tree-lined block on Linden Lane, between Oak and Birch Avenues. We are a few blocks from the Green line train and the Elm Road bus route, and we offer flexible hourly childcare, making it as easy as possible for busy parents on the go to arrange their children's care.</p>
  <p>We invite you to learn more about us and hope you will visit us soon!</p>
</div>

<section class="news">
  <h2>NEWS:</h2>
  <p>We are thrilled to have found a new cheerful space with a private backyard! It's large, sunny, and filled with outdoor play equipment such as a toddler slide, sand/water activity table, and lots of toys!</p>
  <p>Please stay tuned for updates on our program and services as we say goodbye to Winter and hello to Spring!</p>
</section>

<section class="card card-learning">
  <h3>LEARNING</h3>
  <p>We develop age-appropriate activities that introduce and strengthen academic and social skills.</p>
</section>
<section class="card card-creativity">
  <h3>CREATIVITY</h3>
  <p>We offer children a wide range of creative opportunities including art projects, toddler yoga lessons, afternoon tea parties, dress up play, and a large selection of books and games.</p>
</section>
<section class="card card-sharing">
  <h3>SHARING</h3>
  <p>We strive to include enrichment activities that extend your child's understanding of the world and their role in it. During our tea parties, for instance, we teach and emphasize good manners so that your child can learn their benefits as they grow.</p>
</section>

<div class="figure fig-pencil" role="img" aria-label="Cartoon boy riding a giant pencil"></div>
<div class="figure fig-painter" role="img" aria-label="Cartoon girl painting under a rainbow"></div>
<div class="figure fig-pair" role="img" aria-label="Two cartoon children drawing together"></div>

<footer class="footer">
  <span>© Maple Nook Kidcare 2014</span>
  <span>Policy</span>
</footer>
</body>
</html>
```